Personalized Technology Company Needs a Business Card

I need a double-sided business card. Both sides will have the logo, and the contact information. One side will be black, with the white / gray logo, and the other will be white, with the black / gray logo. The black side will have the text "Custom Gaming PC's" and will have a water-cooled gaming PC image. The white side will have the text "Custom Business Computers & Consulting", and will have a business / enterprise PC image. Feel free to add a conservative image in the background, while the color remains unchanged. I'm uploading the base logo (transparent), so you can modify the colors, both the finished colored logos and an idea of ​​the business card (with the current information, just missing the website, which is www.velmorisystems.com, please add it.) Thank you so much for your effort, I'll be specting your cool designs. Good Luck!

Target Market(s)

Gamers & Entrepreneurs / Business Owners / Chief Technology Officers

Industry/Entity Type

Technology Equipment

Contact Information for Business Card

I need a double-sided business card. Both sides will have the logo, and the contact information. One side will be black, with the white/gray logo, and the other one will be white, with the black/gray logo. The black side will have the text "Custom Gaming PC's" and will have a water-cooled gaming PC image. The white side will have the text "Custom Business Computers & Consulting", and will have a business/enterprise PC image. Feel free to add a conservative image in the background, whilst the color remains unchanged.

I'm uploading the base logo (transparent), so you can modify the colors, both the finished colored logos and an idea of the business card (with the actual information, just missing the website, which is www.velmorisystems.com, please add it.)

Thank you so much for your effort, I'll be specting your cool designs. Good Luck!

Font styles to use
Serif

Colors
000000
757575
ffffff

Requirements
Must have
• Please See Description
Nice to have
• Please See Description
Should not have
• Please See Description

```html
<!DOCTYPE html>
<html lang="en">
<head>
<meta charset="utf-8">
<title>Velmori Systems — Business Card</title>
<link rel="stylesheet" href="https://fonts.googleapis.com/css2?family=Poppins:wght@300;400;500&family=Tinos&display=swap">
<style>
  :root {
    --stage: #2b2c2e;
    --card-dark: #1c1c1c;
    --card-light: #ffffff;
    --ink-light: #f2f2f2;
    --ink-dark: #111111;
    --accent: #a89a88;
    --muted: #757575;
    --gear-dark: #2a2a2a;
    --gear-light: #d9d6d2;
  }
  * { box-sizing: border-box; margin: 0; padding: 0; }
  html, body { width: 1200px; height: 900px; overflow: hidden; }
  body {
    background: var(--stage);
    font-family: "Poppins", sans-serif;
    display: flex;
    flex-direction: column;
    align-items: center;
    justify-content: center;
    gap: 40px;
  }
  .card {
    position: relative;
    width: 700px;
    height: 400px;
    box-shadow: 0 10px 30px rgba(0,0,0,.45);
    overflow: hidden;
  }
  .card--front { background: var(--card-dark); color: var(--ink-light); }
  .card--back { background: var(--card-light); color: var(--ink-dark); }

  .card__backdrop {
    position: absolute;
    left: 20px; top: 10px;
    width: 320px; height: 230px;
    border-radius: 50%;
  }
  .card--front .card__backdrop { background: radial-gradient(circle, var(--gear-dark) 0%, transparent 70%); }
  .card--back .card__backdrop { background: radial-gradient(circle, var(--gear-light) 0%, transparent 70%); }

  .card__product {
    position: absolute;
    left: 70px; top: 40px;
    width: 230px; height: 170px;
    border-radius: 6px;
  }
  .card--front .card__product { background: linear-gradient(135deg, #7a1014 0%, #2c2c2c 45%, #6b7a2a 100%); }
  .card--back .card__product { background: linear-gradient(135deg, #202225 0%, #3a3d42 45%, #1e5fb0 100%); }

  .card__tagline {
    position: absolute;
    left: 50px; top: 235px;
    font-family: "Tinos", serif;
    text-transform: uppercase;
    font-size: 17px;
    letter-spacing: 1px;
    line-height: 1.35;
  }
  .card--front .card__tagline { color: #6a6a6a; }
  .card--back .card__tagline { color: var(--ink-dark); }

  .card__info {
    position: absolute;
    right: 45px; top: 70px;
    width: 330px;
    text-align: right;
  }
  .brand {
    display: inline-flex;
    align-items: center;
    gap: 10px;
    font-size: 24px;
    font-weight: 500;
    letter-spacing: 4px;
  }
  .brand__dot {
    width: 26px; height: 26px;
    border-radius: 50%;
    background: var(--accent);
  }
  .person__name {
    margin-top: 34px;
    font-size: 28px;
    font-weight: 300;
  }
  .person__role {
    display: flex;
    align-items: center;
    justify-content: flex-end;
    gap: 10px;
    font-size: 11px;
    color: var(--accent);
    margin-top: 2px;
  }
  .person__rule { width: 90px; height: 1px; background: var(--accent); }
  .contacts {
    list-style: none;
    margin-top: 18px;
    font-size: 13px;
    line-height: 25px;
  }
  .contacts li {
    display: flex;
    justify-content: flex-end;
    align-items: center;
    gap: 12px;
  }
  .contacts svg { width: 14px; height: 14px; flex: none; }
  .card--front .contacts svg { fill: var(--ink-light); stroke: var(--ink-light); }
  .card--back .contacts svg { fill: var(--muted); stroke: var(--muted); }
</style>
</head>
<body>

<section class="card card--front">
  <div class="card__backdrop"></div>
  <div class="card__product" role="img" aria-label="Water-cooled gaming PC with red lighting beside a monitor showing a game scene"></div>
  <p class="card__tagline">Custom Gaming PC's</p>
  <div class="card__info">
    <div class="brand"><span class="brand__dot"></span>VELMORI SYSTEMS</div>
    <p class="person__name">Daniel Reyes Moran</p>
    <p class="person__role"><span class="person__rule"></span>CEO &amp; Co-Founder</p>
    <ul class="contacts">
      <li>+52 5812-3307<svg viewBox="0 0 16 16"><path stroke="none" d="M4 1l3 3-2 2c1 2 3 4 5 5l2-2 3 3-2 2C7 14 2 9 2 3z"/></svg></li>
      <li>+52 55-4190-6618<svg viewBox="0 0 16 16"><rect x="4" y="1" width="8" height="14" rx="1.5" fill="none" stroke-width="1.5"/></svg></li>
      <li>contact@velmorisystems.com<svg viewBox="0 0 16 16"><path stroke="none" d="M1 3h14v10H1z"/></svg></li>
      <li>www.velmorisystems.com<svg viewBox="0 0 16 16" fill="none"><circle cx="8" cy="8" r="6.5" fill="none" stroke-width="1.5"/><path d="M1.5 8h13M8 1.5c-3 3.5-3 9.5 0 13M8 1.5c3 3.5 3 9.5 0 13" fill="none" stroke-width="1.2"/></svg></li>
    </ul>
  </div>
</section>

<section class="card card--back">
  <div class="card__backdrop"></div>
  <div class="card__product" role="img" aria-label="Business desktop tower with a flat monitor showing a blue screen"></div>
  <p class="card__tagline">Custom Business<br>Computers &amp; Consulting</p>
  <div class="card__info">
    <div class="brand"><span class="brand__dot"></span>VELMORI SYSTEMS</div>
    <p class="person__name">Daniel Reyes Moran</p>
    <p class="person__role"><span class="person__rule"></span>CEO &amp; Co-Founder</p>
    <ul class="contacts">
      <li>+52 5812-3307<svg viewBox="0 0 16 16"><path stroke="none" d="M4 1l3 3-2 2c1 2 3 4 5 5l2-2 3 3-2 2C7 14 2 9 2 3z"/></svg></li>
      <li>+52 55-4190-6618<svg viewBox="0 0 16 16"><rect x="4" y="1" width="8" height="14" rx="1.5" fill="none" stroke-width="1.5"/></svg></li>
      <li>contact@velmorisystems.com<svg viewBox="0 0 16 16"><path stroke="none" d="M1 3h14v10H1z"/></svg></li>
      <li>www.velmorisystems.com<svg viewBox="0 0 16 16" fill="none"><circle cx="8" cy="8" r="6.5" fill="none" stroke-width="1.5"/><path d="M1.5 8h13M8 1.5c-3 3.5-3 9.5 0 13M8 1.5c3 3.5 3 9.5 0 13" fill="none" stroke-width="1.2"/></svg></li>
    </ul>
  </div>
</section>

</body>
</html>
```